Exhibition Stand Design for innovative Social Business

We are an innovative social business empowering people to value nature through ZUN, a complementary digital currency. We have attached the TEK_ZUN branding document, and are needing a design for our exhibition stand (https://fairbuildlab.com/produit/stand-parapluie-classic-pvc-3x4c/. The attached doc mocks up a stand on page 32, though we would like some messaging included, in line with our website www.tekzun.ch. You will see there how the branding concept has been implemented with the TEK:GROW, SHARE, THRIVE wording, as well as Everyone wins. Our green colours are included in the branding document. Many thanks!

Industry/Entity Type

Environment

Font styles to use
Other font styles liked:
• As per our attached fonts

Requirements
Must have
• Our attached branding guidelines gives our look and feel - Innovative / Dynamic / Vibrant / Reliable / Accessible / Connected.

```html
<!DOCTYPE html>
<html lang="en">
<head>
<meta charset="utf-8">
<title>TEK ZUN – Better for you, better for the planet</title>
<link href="https://fonts.googleapis.com/css2?family=Archivo:wght@400;800;900&display=swap" rel="stylesheet">
<style>
  :root {
    --aqua: #5ce6c6;
    --mint: #3fe98f;
    --green: #2fe864;
    --leaf-light: #a6e25a;
    --leaf-mid: #5fbf3a;
    --leaf-deep: #2f7d2a;
    --ink: #0d0d0d;
    --white: #ffffff;
  }
  * { margin: 0; padding: 0; box-sizing: border-box; }
  html, body { width: 1200px; height: 657px; overflow: hidden; }
  body { font-family: "Archivo", Arial, sans-serif; }

  .banner {
    position: relative;
    width: 1200px;
    height: 657px;
    overflow: hidden;
    background: linear-gradient(90deg, var(--aqua) 0%, var(--mint) 25%, var(--green) 48%, var(--green) 100%);
  }

  .forest-photo {
    position: absolute;
    top: 0;
    right: 0;
    width: 680px;
    height: 657px;
    background:
      linear-gradient(90deg, var(--green) 0%, rgba(47,232,100,0) 35%),
      radial-gradient(ellipse at 45% 10%, #f3ffd0 0%, rgba(243,255,208,0) 40%),
      linear-gradient(180deg, var(--leaf-light) 0%, var(--leaf-mid) 45%, var(--leaf-deep) 100%);
  }

  .brand-name {
    position: absolute;
    top: 22px;
    right: 45px;
    font-weight: 900;
    font-size: 104px;
    line-height: 1;
    letter-spacing: -1px;
    color: var(--ink);
  }

  .tagline { position: absolute; left: 67px; top: 0; }

  .tagline-label,
  .tagline-value {
    position: absolute;
    left: 0;
    white-space: nowrap;
    line-height: 1;
  }

  .tagline-label {
    font-weight: 800;
    font-size: 46px;
    color: var(--ink);
    letter-spacing: 0.5px;
  }

  .tagline-label .colon { margin-left: 10px; }

  .tagline-value {
    font-weight: 400;
    font-size: 56px;
    color: var(--white);
  }

  .label-you    { top: 262px; }
  .value-you    { top: 330px; }
  .label-planet { top: 420px; }
  .value-planet { top: 488px; }
</style>
</head>
<body>
  <main class="banner">
    <div class="forest-photo" role="img" aria-label="Woman in a white top raising her arms among sunlit green forest trees"></div>

    <div class="brand-name">TEK ZUN</div>

    <div class="tagline">
      <p class="tagline-label label-you">BETTER<span class="colon">:</span></p>
      <p class="tagline-value value-you">FOR YOU</p>
      <p class="tagline-label label-planet">BETTER<span class="colon">:</span></p>
      <p class="tagline-value value-planet">FOR THE PLANET</p>
    </div>
  </main>
</body>
</html>
```